Machine shop needs a brochure designed

Would like a tri-fold professional looking brochure that tells about our business and our capabilities. We are a family-owned business with over 50 years of experience in precision manufacturing. We specialize in close-tolerance tooling and serve a diverse array of industries. Our colors are red, black, white, and gray. The final design should make a great impression and spotlight our capabilities and quality.

Target Market(s)

Manufacturing industries needing tooling

Industry/Entity Type

Machining, grinding, manufacturing

Font styles to use
Serif

Colors
EB3D1F
EC4F4E
F09395
F8D3D4
FCEDEE

Requirements
Must have
• Logo, colors are red, black, white, gray
Nice to have
• Images of CNC process or machining/grinding metal parts.

```html
<!DOCTYPE html>
<html lang="en">
<head>
<meta charset="utf-8">
<title>Corvane Industries – Tri-fold Brochure</title>
<link rel="stylesheet" href="https://fonts.googleapis.com/css2?family=Playfair+Display+SC:wght@700;900&family=Montserrat:wght@400;500;700&family=Raleway:wght@400;700&display=swap">
<style>
  :root{
    --red:#c8101e;
    --red-deep:#9e0a14;
    --red-bright:#e8121f;
    --maroon:#4a1416;
    --ink:#2b1a14;
    --black:#111;
    --white:#ffffff;
    --paper:#f3f3f3;
    --stage:#e2e2e2;
    --steel:#8a8a88;
  }
  *{box-sizing:border-box;margin:0;padding:0}
  html,body{width:1200px;height:2383px;overflow:hidden;background:var(--stage)}
  .stage{position:relative;width:1200px;height:2383px}
  .spread{position:absolute;left:30px;top:750px;width:1140px;height:880px;display:flex;box-shadow:0 10px 30px rgba(0,0,0,.18)}
  .panel{position:relative;width:380px;height:880px;overflow:hidden}
  .panel > svg.bg{position:absolute;inset:0}

  /* about panel */
  .about-text{position:absolute;left:22px;top:248px;width:340px;color:var(--white);
    font:400 16.8px/21.6px "Raleway",sans-serif;text-align:justify;hyphens:none}
  .about-text p + p{margin-top:21px}
  .about-text strong{font-weight:700}

  /* contact panel */
  .offer-box{position:absolute;left:44px;top:388px;width:288px;height:132px;border:1.5px solid var(--black);
    border-radius:4px;background:var(--white);display:flex;align-items:center;justify-content:center;text-align:center;
    font:500 19px/24px "Montserrat",sans-serif;color:var(--black);text-transform:uppercase}
  .company-name{position:absolute;left:0;width:380px;top:540px;text-align:center;
    font:500 21px/1 "Montserrat",sans-serif;color:var(--black)}
  .brand-mark{position:absolute;left:0;width:380px;top:598px;display:flex;align-items:center;justify-content:center;gap:12px}
  .brand-mark .dot{width:34px;height:34px;border-radius:50%;background:var(--red-bright)}
  .brand-mark .word{font:700 26px/1 "Montserrat",sans-serif;color:var(--red-bright)}
  .brand-rule{position:absolute;left:40px;width:300px;top:668px;height:1px;background:linear-gradient(90deg,transparent,#999,transparent)}
  .contact-icons{position:absolute;left:0;width:380px;top:690px;display:flex;justify-content:center;gap:8px}
  .contact-icons svg{width:30px;height:30px}
  .contact-lines{position:absolute;left:0;width:380px;top:735px;text-align:center;
    font:500 17px/26px "Montserrat",sans-serif;color:var(--black)}

  /* cover panel */
  .cover-title{position:absolute;left:0;width:380px;top:58px;text-align:center;color:var(--white);
    font:900 54px/74px "Playfair Display SC",serif;letter-spacing:1px}
  .cover-line{position:absolute;left:0;width:380px;text-align:center;color:var(--ink);font-family:"Montserrat",sans-serif}
  .cover-line.light{top:640px;font-weight:400;font-size:38px}
  .cover-line.bold{font-weight:700;font-size:38px;letter-spacing:.5px}
  .cover-line.l2{top:690px}
  .cover-line.l3{top:740px}
  .url-pill{position:absolute;left:48px;top:816px;width:296px;height:36px;border-radius:18px;background:var(--red-bright);
    color:var(--white);font:500 21px/36px "Montserrat",sans-serif;text-align:center}
</style>
</head>
<body>
<main class="stage">
  <section class="spread" aria-label="Corvane Industries tri-fold brochure, inside spread">

    <!-- About panel -->
    <article class="panel panel-about">
      <svg class="bg" width="380" height="880" viewBox="0 0 380 880">
        <defs>
          <linearGradient id="aboutPhoto" x1="0" y1="0" x2="1" y2="1">
            <stop offset="0" stop-color="#5c5c5c"/><stop offset=".6" stop-color="#a8a8a8"/><stop offset="1" stop-color="#3a3a3a"/>
          </linearGradient>
          <linearGradient id="aboutRed" x1="0" y1="0" x2="0" y2="1">
            <stop offset="0" stop-color="#c8101e"/><stop offset="1" stop-color="#a40b16"/>
          </linearGradient>
        </defs>
        <rect width="380" height="300" fill="url(#aboutPhoto)" role="img" aria-label="Photo: plasma cutter cutting a steel sheet with sparks"/>
        <path d="M0,228 Q170,140 380,232 L380,880 L0,880Z" fill="#ffffff"/>
        <path d="M0,240 Q175,160 380,248 L380,880 L0,880Z" fill="url(#aboutRed)"/>
      </svg>
      <div class="about-text">
        <p><strong>About Corvane Industries, Inc.</strong> is a privately owned company with over fifty years of experience in precision manufacturing. Products manufactured include components for a national defense program during Operation Desert Storm, machine gun barrels, close tolerance can tooling, conveyor slats and rollers, molds, various production tooling for several national industries, pump housings for the gasoline industry, aviation and automotive manufacturing, and various precision machining and grinding jobs. Currently, Corvane Industries, Inc. is working with a group of physicians to develop and patent various surgical devices for use in Orthopedic and General Vascular surgeries.</p>
        <p>We at Corvane Industries, Inc. look forward to the opportunity to work with you and quote any projects you might want us to look at. We take a “Quality first” approach to all of our jobs and we have the determination to get the job done according to our clients’ timelines. We are always looking for opportunities to form new alliances and friendships with prospective clients.</p>
      </div>
    </article>

    <!-- Contact panel -->
    <article class="panel panel-contact">
      <svg class="bg" width="380" height="880" viewBox="0 0 380 880">
        <defs>
          <linearGradient id="millPhoto" x1="0" y1="0" x2="0" y2="1">
            <stop offset="0" stop-color="#1f242b"/><stop offset=".5" stop-color="#3b4048"/><stop offset="1" stop-color="#15181c"/>
          </linearGradient>
        </defs>
        <rect width="380" height="880" fill="var(--paper)"/>
        <path d="M0,0 H380 V268 Q310,372 180,368 Q60,362 0,312Z" fill="#c8101e"/>
        <path d="M0,0 H380 V255 Q305,358 180,354 Q60,350 0,300Z" fill="#ffffff"/>
        <path d="M0,0 H380 V248 Q300,350 180,346 Q60,342 0,294Z" fill="url(#millPhoto)" role="img" aria-label="Photo: CNC end mill cutting metal with chips flying"/>
      </svg>
      <div class="offer-box">We are now offering<br>personalized delivery<br>on orders totaling<br>$100 or more.</div>
      <div class="company-name">Corvane Industries, Inc.</div>
      <div class="brand-mark"><span class="dot"></span><span class="word">Corvane</span></div>
      <div class="brand-rule"></div>
      <div class="contact-icons">
        <svg viewBox="0 0 30 30" aria-label="Location"><circle cx="15" cy="15" r="13" fill="none" stroke="#e8121f" stroke-width="2"/><path d="M15 7a5 5 0 0 0-5 5c0 4 5 10 5 10s5-6 5-10a5 5 0 0 0-5-5z" fill="#222"/><circle cx="15" cy="12" r="1.8" fill="#fff"/></svg>
        <svg viewBox="0 0 30 30" aria-label="Phone"><circle cx="15" cy="15" r="13" fill="none" stroke="#e8121f" stroke-width="2"/><path d="M10.5 8.5l2.6-.4 1.5 3.4-1.6 1.2a9 9 0 0 0 4.3 4.3l1.2-1.6 3.4 1.5-.4 2.6c-6 .5-11.5-5-11-11z" fill="#222"/></svg>
        <svg viewBox="0 0 30 30" aria-label="Email"><circle cx="15" cy="15" r="13" fill="none" stroke="#e8121f" stroke-width="2"/><rect x="8" y="10" width="14" height="10" rx="1" fill="#222"/><path d="M8.5 10.5L15 15.5l6.5-5" fill="none" stroke="#fff" stroke-width="1.3"/></svg>
      </div>
      <div class="contact-lines">
        1480 Millbrook Rd. Ashford,<br>TN 37100<br>Phone: 615.555.0148<br>quotes@corvaneindustries.net
      </div>
    </article>

    <!-- Cover panel -->
    <article class="panel panel-cover">
      <svg class="bg" width="380" height="880" viewBox="0 0 380 880">
        <defs>
          <linearGradient id="coverRed" x1="0" y1="0" x2="0" y2="1">
            <stop offset="0" stop-color="#c40d1b"/><stop offset="1" stop-color="#e0141f"/>
          </linearGradient>
          <linearGradient id="coverWhite" x1="0" y1="0" x2="0" y2="1">
            <stop offset="0" stop-color="#ececec"/><stop offset="1" stop-color="#f7f7f7"/>
          </linearGradient>
          <linearGradient id="pipes" x1="0" y1="0" x2="1" y2="0">
            <stop offset="0" stop-color="#b80f18"/><stop offset=".45" stop-color="#d8202a"/><stop offset=".6" stop-color="#8d8c88"/><stop offset="1" stop-color="#5f5e5a"/>
          </linearGradient>
        </defs>
        <rect width="380" height="880" fill="url(#coverWhite)"/>
        <path d="M0,0 H380 V420 L0,588Z" fill="url(#coverRed)"/>
        <path d="M0,588 L380,420 L380,438 L0,606Z" fill="#ffffff"/>
        <path d="M0,596 L380,428 L380,436 L0,604Z" fill="var(--maroon)"/>
        <circle cx="190" cy="466" r="176" fill="#ffffff"/>
        <circle cx="190" cy="466" r="168" fill="url(#pipes)" role="img" aria-label="Photo: stacked ends of red and steel tubes"/>
      </svg>
      <h1 class="cover-title">Corvane<br>Industries</h1>
      <div class="cover-line light">PRECISE,</div>
      <div class="cover-line bold l2">HIGH-QUALITY</div>
      <div class="cover-line bold l3">COMPONENTS</div>
      <div class="url-pill">www.corvaneindustries.net</div>
    </article>

  </section>
</main>
</body>
</html>
```